Update Letterhead for Harbor Vale Advisors

We need a modernized and updated letterhea. We DO NOT want to change fonts, we want incorporate the logo and words better and make a sleeker and elegant logo catering to wealthy clients. Harbor is a wealth management firm catering to business owners, physicians, and high net wort clientele. Our letterhead should have strength and elegance and cater to that market. Guaranteed payment.

Requirements
Must have
• PLEASE NOTE THAT THE LOGO USED IN THE ORIGINAL DESIGNS ARE INCORRECT! Please update to the new logo!
• We also changed our color scheme to grey and gold and black. Please refer to website www.harborva-example.com to see what I mean as we want to update to that rather than the dark blue. (Most likely grey and gold)

```html
<!DOCTYPE html>
<html lang="en">
<head>
<meta charset="utf-8">
<title>Harbor Vale Advisors — Letterhead</title>
<link href="https://fonts.googleapis.com/css2?family=Cinzel:wght@700&family=PT+Sans:wght@400&display=swap" rel="stylesheet">
<style>
  :root {
    --band-grey: #818286;
    --band-frame: #c49a6c;
    --gold: #d3ae62;
    --ink: #111111;
    --paper: #ffffff;
    --ghost: #f1f1f1;
  }
  * { margin: 0; padding: 0; box-sizing: border-box; }
  html, body { width: 848px; height: 1200px; overflow: hidden; background: var(--paper); }
  .letterhead {
    position: relative;
    width: 848px;
    height: 1200px;
    background: var(--paper);
    font-family: "PT Sans", Arial, sans-serif;
    color: var(--ink);
    overflow: hidden;
  }
  .masthead {
    position: absolute;
    left: 0; top: 0;
    width: 848px; height: 152px;
    background: var(--band-grey);
    border: 6px solid var(--band-frame);
  }
  .brand-dot {
    position: absolute;
    left: 85px; top: 21px;
    width: 108px; height: 108px;
    border-radius: 50%;
    background: var(--gold);
  }
  .brand-name {
    position: absolute;
    left: 205px; top: 26px;
    font-family: "Cinzel", "Times New Roman", serif;
    font-weight: 700;
    font-size: 47px;
    line-height: 1;
    color: var(--gold);
    letter-spacing: 0.5px;
    white-space: nowrap;
  }
  .brand-rule {
    position: absolute;
    left: 211px; top: 92px;
    width: 286px; height: 9px;
    background: var(--paper);
  }
  .brand-sub {
    position: absolute;
    left: 502px; top: 84px;
    font-family: "Cinzel", "Times New Roman", serif;
    font-weight: 700;
    font-size: 24px;
    line-height: 1;
    color: var(--gold);
    white-space: nowrap;
  }
  .ghost-mark {
    position: absolute;
    inset: 0;
    pointer-events: none;
  }
  .ghost-mark text {
    font-family: "Cinzel", "Times New Roman", serif;
    font-weight: 700;
    font-size: 150px;
    fill: var(--ghost);
  }
  .signature-rule {
    position: absolute;
    top: 1022px; height: 7px;
    background: var(--gold);
  }
  .signature-rule.left { left: 0; width: 263px; }
  .signature-rule.right { left: 606px; width: 242px; }
  .advisor-name {
    position: absolute;
    left: 0; width: 848px; top: 1013px;
    text-align: center;
    font-size: 18px;
  }
  .advisor-role, .advisor-email {
    position: absolute;
    left: 0; width: 848px;
    text-align: center;
    font-size: 15.5px;
  }
  .advisor-role { top: 1048px; }
  .advisor-email { top: 1069px; }
  .office {
    position: absolute;
    top: 1100px;
    font-size: 16px;
    line-height: 21px;
  }
  .office.downtown { left: 42px; }
  .office.westside { left: 594px; }
  .website {
    position: absolute;
    left: 0; width: 848px; top: 1141px;
    padding-left: 20px;
    text-align: center;
    font-size: 16px;
  }
</style>
</head>
<body>
<div class="letterhead">
  <header class="masthead">
    <div class="brand-dot" aria-hidden="true"></div>
    <div class="brand-name">HARBOR VALE</div>
    <div class="brand-rule" aria-hidden="true"></div>
    <div class="brand-sub">ADVISORS</div>
  </header>

  <svg class="ghost-mark" width="848" height="1200" viewBox="0 0 848 1200" aria-hidden="true">
    <text x="340" y="540" text-anchor="middle" transform="rotate(-15 340 500)">HARBOR</text>
    <text x="460" y="745" text-anchor="middle" transform="rotate(-15 460 700)">VALE</text>
  </svg>

  <footer class="letter-footer">
    <div class="signature-rule left"></div>
    <div class="signature-rule right"></div>
    <div class="advisor-name">Margaret Lowell Prescott, CFP, MSFS, AEP</div>
    <div class="advisor-role">PRESIDENT &amp; FINANCIAL ADVISOR Tel. 915.555.0142</div>
    <div class="advisor-email">mprescott@harborva-example.com</div>
    <address class="office downtown" style="font-style:normal">
      Downtown Office<br>210 North Mesa Street, Suite 900<br>El Paso, TX 79901
    </address>
    <div class="website">www.harborva-example.com</div>
    <address class="office westside" style="font-style:normal">
      Westside Office<br>5120 Ridgecrest Drive, Suite B<br>El Paso, TX 79922
    </address>
  </footer>
</div>
</body>
</html>
```